Business Card Design needed for logo design project

Our company needs a Business Card Design. Please refer to our original project in the link above.
Dorian Whitlock
Broker

W: Grandvistaestates.com
P: 214-555-0187
F: 267-555-0142
E: dorianwhitlock@ferncrestmail.com
A: North Dallas Office

Name Spelling update , sorry Dorian Whitlock card is double sided

```html
<!DOCTYPE html>
<html lang="en">
<head>
<meta charset="utf-8">
<title>Grandvista Estates – Business Card Options</title>
<link rel="stylesheet" href="https://fonts.googleapis.com/css2?family=Crimson+Pro:wght@400;600&display=swap">
<style>
  :root {
    --sheet: #ffffff;
    --charcoal: #4a4847;
    --paper: #fafafa;
    --green: #0fa64f;
    --gold: #a8854f;
    --gold-text: #a98a5a;
    --panel-text: #ffffff;
  }
  * { box-sizing: border-box; margin: 0; padding: 0; }
  html, body {
    width: 1200px; height: 1050px; overflow: hidden;
    background: var(--sheet);
  }
  .sheet { position: relative; width: 1200px; height: 1050px; }

  .card {
    position: absolute;
    width: 587px; height: 335px;
    overflow: hidden;
  }
  .card--dark { background: var(--charcoal); }
  .card--light { background: var(--paper); }

  .col-1 { left: 7px; }
  .col-2 { left: 607px; }
  .row-1 { top: 7px; }
  .row-2 { top: 357px; }
  .row-3 { top: 707px; }

  .brand {
    position: absolute;
    left: 0; top: 0;
    width: 360px; height: 335px;
    display: flex; flex-direction: column;
    align-items: center; justify-content: center;
    gap: 18px;
  }
  .brand__dot {
    width: 18px; height: 18px; border-radius: 50%;
    background: var(--gold);
  }
  .brand__name {
    font-family: "Crimson Pro", Georgia, serif;
    font-weight: 600;
    font-size: 27px;
    line-height: 1.15;
    letter-spacing: 2px;
    text-transform: uppercase;
    text-align: center;
    color: var(--gold-text);
  }

  .details {
    position: absolute;
    display: flex; flex-direction: column;
    justify-content: space-between;
    padding: 20px 16px 18px 21px;
    color: var(--panel-text);
    font-family: "Crimson Pro", Georgia, serif;
    text-transform: uppercase;
  }
  .details--green { background: var(--green); }
  .details--gold { background: var(--gold); }

  .details--low { left: 379px; top: 166px; width: 208px; height: 169px; }
  .details--tall { left: 387px; top: 156px; width: 200px; height: 179px; }
  .details--square { left: 359px; top: 57px; width: 228px; height: 228px; }

  .details__name {
    font-size: 15px; font-weight: 600; letter-spacing: 1px;
  }
  .details__role {
    margin-top: 6px;
    font-size: 8.5px; letter-spacing: 0.8px;
  }
  .details__contact {
    list-style: none;
    font-size: 8.5px; line-height: 14px; letter-spacing: 0.3px;
  }
</style>
</head>
<body>
<main class="sheet">

  <section class="card card--dark col-1 row-1">
    <div class="brand"><span class="brand__dot"></span><p class="brand__name">Grandvista<br>Estates</p></div>
    <div class="details details--green details--low">
      <div><p class="details__name">Dorian Whitlock</p><p class="details__role">Broker</p></div>
      <ul class="details__contact">
        <li>P: 214-555-0187</li><li>F: 267-555-0142</li>
        <li>W: Grandvistaestates.com</li><li>E: dorianwhitlock@ferncrestmail.com</li>
      </ul>
    </div>
  </section>

  <section class="card card--dark col-2 row-1">
    <div class="brand"><span class="brand__dot"></span><p class="brand__name">Grandvista<br>Estates</p></div>
    <div class="details details--gold details--tall">
      <div><p class="details__name">Dorian Whitlock</p><p class="details__role">Broker</p></div>
      <ul class="details__contact">
        <li>P: 214-555-0187</li><li>F: 267-555-0142</li>
        <li>W: Grandvistaestates.com</li><li>E: dorianwhitlock@ferncrestmail.com</li>
      </ul>
    </div>
  </section>

  <section class="card card--dark col-1 row-2">
    <div class="brand"><span class="brand__dot"></span><p class="brand__name">Grandvista<br>Estates</p></div>
    <div class="details details--gold details--square">
      <div><p class="details__name">Dorian Whitlock</p><p class="details__role">Broker</p></div>
      <ul class="details__contact">
        <li>P: 214-555-0187</li><li>F: 267-555-0142</li>
        <li>W: Grandvistaestates.com</li><li>E: dorianwhitlock@ferncrestmail.com</li>
      </ul>
    </div>
  </section>

  <section class="card card--dark col-2 row-2">
    <div class="brand"><span class="brand__dot"></span><p class="brand__name">Grandvista<br>Estates</p></div>
    <div class="details details--green details--square">
      <div><p class="details__name">Dorian Whitlock</p><p class="details__role">Broker</p></div>
      <ul class="details__contact">
        <li>P: 214-555-0187</li><li>F: 267-555-0142</li>
        <li>W: Grandvistaestates.com</li><li>E: dorianwhitlock@ferncrestmail.com</li>
      </ul>
    </div>
  </section>

  <section class="card card--light col-1 row-3">
    <div class="brand"><span class="brand__dot"></span><p class="brand__name">Grandvista<br>Estates</p></div>
    <div class="details details--green details--square">
      <div><p class="details__name">Dorian Whitlock</p><p class="details__role">Broker</p></div>
      <ul class="details__contact">
        <li>P: 214-555-0187</li><li>F: 267-555-0142</li>
        <li>W: Grandvistaestates.com</li><li>E: dorianwhitlock@ferncrestmail.com</li>
      </ul>
    </div>
  </section>

  <section class="card card--light col-2 row-3">
    <div class="brand"><span class="brand__dot"></span><p class="brand__name">Grandvista<br>Estates</p></div>
    <div class="details details--gold details--square">
      <div><p class="details__name">Dorian Whitlock</p><p class="details__role">Broker</p></div>
      <ul class="details__contact">
        <li>P: 214-555-0187</li><li>F: 267-555-0142</li>
        <li>W: Grandvistaestates.com</li><li>E: dorianwhitlock@ferncrestmail.com</li>
      </ul>
    </div>
  </section>

</main>
</body>
</html>
```